Turn Fold-Kit Pal from a practical essential into must have shopping accessory for Carrimax

Our product is a folding box which opens from a small flat-pack brief case into a crate-style box that holds in excess of 20kg. It has been designed as a 'box for life' alternative to 'bags for life'. We want to make the exterior of our product visually appealing to consumers.

Our concept is for the box to look like a satchel or other type of bag when it is closed and something different when it is open. This could be anything! Our ideas include floral (Mira Pellow inspired), patterns, stripes, spots, or mural/print designs to look like something different such as a wicker hamper/basket or old style wooden Tea/Shipping crate when open, etc. Use your imagination! The winning design will have broad market appeal and be feminine or gender natural.

The winning design must be produced in two parts:

1. With the box folded and closed. We want this to look like an old style school satchel or other type of bag. The areas that this part of the design needs to cover are highlighted on the design sheet attached. Note that these areas form the base of the box when it is ‘open as a crate’, so it is possible to incorporate two designs

2. With the box open as a crate. We want a design that works around the full 360 degree aspect of the box. This could be anything. The design will need to break and be repeated in some areas so it flows across the box when it is put together from a flat sheet (see design sheet and below for more information)

This design competition is for decorating the outside of the box only and the base colour of the box will be white.

The winning design will be screen printed onto a single flat sheet of plastic and must work with the way the box folds and fixes together during the manufacturing process. In particular:
• The design cannot run into the areas highlighted in blue as these will be covered during the manufacturing process by the handles and side rails. As such blank areas must to be left on the side panels. These must mirror the shape of the end tabs which fold internally (see design sheet)
• The design for the ends of box when it is open will have to be printed in two parts – highlighted in pink on design sheet. As such the design/pattern will need to be repeated on the external tabs along the long edges of the box to match the design on the end panels of the box as these fold over the outer ends of the box when it is put together
• Our website address must be incorporated into the design to be visible but not dominant
• Our Design/Patent number must be discretely but visibly incorporated into the design
• The design will be screen printed onto a single flat sheet of plastic so final designs will need to be supplied as Coral Draw or ‘AI’ format in CMYK

We have included a design sheet as an attachment which provides the dimensions of our box as a single flat sheet. A second design sheet is attached which highlights the areas that need to be left blank, and where designs/patterns need to break & repeat so they work when the box is put together. We have also made a couple of short videos to show this:

https://www.vaultlyn.com/sh/7qpx2mw9rtk04za/BBXQmel3KcRwTnZdYhPjVsLoQ

if you have any questions about the brief or competition, please get in touch with me - tomas@carrimax.co.uk

i look forward to viewing your submissions, good luck!

```html
<!DOCTYPE html>
<html lang="en">
<head>
<meta charset="utf-8">
<title>Fold-Kit Pal – Open Crate Print Sheet</title>
<link rel="stylesheet" href="https://fonts.googleapis.com/css2?family=Open+Sans:wght@400;700&display=swap">
<style>
  :root {
    --backdrop-light: #f1f1f2;
    --backdrop-mid: #c9cacc;
    --backdrop-dark: #a9abae;
    --sheet-white: #ffffff;
    --band-purple: #8a3d92;
    --floral-orange: #f7a65e;
    --floral-lime: #d6e46a;
    --floral-blue: #5f9bd2;
    --floral-purple: #a869b0;
    --sheet-shadow: rgba(0, 0, 0, 0.28);
  }
  html, body {
    margin: 0;
    padding: 0;
    width: 1200px;
    height: 900px;
    overflow: hidden;
  }
  .stage {
    display: block;
    width: 1200px;
    height: 900px;
  }
  .sheet-base { fill: var(--sheet-white); }
  .purple-frame { fill: var(--band-purple); }
  .band-rule { stroke: var(--sheet-white); stroke-width: 2; }
  .fold-rule { stroke: var(--sheet-white); stroke-width: 1.5; }
  .floral-fill { fill: url(#floralTones); }
  .web-address {
    font-family: "Open Sans", sans-serif;
    font-weight: 700;
    font-size: 9px;
    letter-spacing: 3px;
    fill: var(--sheet-white);
  }
  .patent-note {
    font-family: "Open Sans", sans-serif;
    font-weight: 400;
    font-size: 5px;
    fill: var(--sheet-white);
  }
</style>
</head>
<body>
<svg class="stage" viewBox="0 0 1200 900" xmlns="http://www.w3.org/2000/svg">
  <defs>
    <radialGradient id="backdrop" cx="0.6" cy="0.45" r="0.8">
      <stop offset="0" stop-color="var(--backdrop-light)"/>
      <stop offset="0.6" stop-color="var(--backdrop-mid)"/>
      <stop offset="1" stop-color="var(--backdrop-dark)"/>
    </radialGradient>
    <linearGradient id="floralTones" x1="0" y1="0" x2="1" y2="0.6" spreadMethod="reflect">
      <stop offset="0" stop-color="var(--floral-orange)"/>
      <stop offset="0.3" stop-color="var(--floral-lime)"/>
      <stop offset="0.6" stop-color="var(--floral-blue)"/>
      <stop offset="1" stop-color="var(--floral-purple)"/>
    </linearGradient>
    <filter id="sheetShadow" x="-5%" y="-5%" width="110%" height="110%">
      <feDropShadow dx="2" dy="3" stdDeviation="3" flood-color="var(--sheet-shadow)"/>
    </filter>
  </defs>

  <rect class="backdrop" width="1200" height="900" fill="url(#backdrop)"/>

  <g class="crate-sheet" filter="url(#sheetShadow)">
    <path class="sheet-base" d="
      M326 62 H555 L562 44 H623 L630 62 H857 V285 H1017 V338 H997 V348 H1017 V432 H997 V442 H1017 V500 H857
      V722 H630 L623 740 H562 L555 722 H326 V500 H166 V442 H186 V432 H166 V348 H186 V338 H166 V285 H326 Z"/>

    <!-- long side panels -->
    <path class="floral-fill" d="M326 62 H555 L562 44 H623 L630 62 H857 V220 H326 Z" role="img" aria-label="Repeating floral print of orange, lime, blue and purple star-shaped flowers with small dots on white, top side panel"/>
    <path class="floral-fill" d="M326 562 H857 V722 H630 L623 740 H562 L555 722 H326 Z" role="img" aria-label="Repeating floral print of orange, lime, blue and purple star-shaped flowers with small dots on white, bottom side panel"/>

    <!-- end flaps -->
    <path class="floral-fill" d="M166 285 H326 V500 H166 V442 H186 V432 H166 V348 H186 V338 H166 Z" role="img" aria-label="Floral print on left end flap"/>
    <path class="floral-fill" d="M857 285 H1017 V338 H997 V348 H1017 V432 H997 V442 H1017 V500 H857 Z" role="img" aria-label="Floral print on right end flap"/>

    <!-- purple frame around base -->
    <rect class="purple-frame" x="330" y="224" width="523" height="332"/>
    <path class="sheet-base" d="M326 250 L326 272 L346 252 L346 250 Z M857 250 L857 272 L837 252 L837 250 Z M326 534 L326 512 L346 528 L346 534 Z M857 534 L857 512 L837 528 L837 534 Z"/>
    <line class="band-rule" x1="346" y1="252" x2="837" y2="252"/>
    <line class="band-rule" x1="346" y1="528" x2="837" y2="528"/>
    <line class="fold-rule" x1="350" y1="280" x2="350" y2="500"/>
    <line class="fold-rule" x1="833" y1="280" x2="833" y2="500"/>

    <!-- base panels -->
    <rect class="floral-fill" x="370" y="262" width="203" height="260" role="img" aria-label="Floral print on left base panel"/>
    <rect class="floral-fill" x="607" y="262" width="207" height="260" role="img" aria-label="Floral print on right base panel"/>

    <!-- web address -->
    <text class="web-address" x="590" y="241" text-anchor="middle">www.foldkit-pal.com</text>
    <text class="web-address" x="590" y="541" text-anchor="middle" transform="rotate(180 590 538)">www.foldkit-pal.com</text>

    <!-- design / patent number -->
    <text class="patent-note" x="343" y="392" text-anchor="middle" transform="rotate(-90 343 392)">Reg Design No: 4821307 Patent app no GB1607342.5</text>
    <text class="patent-note" x="840" y="392" text-anchor="middle" transform="rotate(90 840 392)">Reg Design No: 4821307 Patent app no GB1607342.5</text>
  </g>
</svg>
</body>
</html>
```